Varga Lillas Physiotherapy Business Card Vienna

We need a business card design for a newly created Physiotherapy company based in Vienna Austria.
We seek a simple, modern, minimalist design without too much color variation. The font should look young/fresh, but definitely not childish or so. Since we are a starting Business, we currently haven't got a logo, if you feel like a logo would fit your design, feel free to use one, but it's not necessary.
Target Market(s)
Healthcare, young and elderly people with mobility issues
Industry/Entity Type
Health And Wellness
Contact Information for Business Card
Name: Lilla Varga
Title description: Physiotherapist
Phone num: +43 664 5290 4816
e-mail: lilla.praxis@brelomail.com
Colors
Designer to choose colors to be used in the design.
Requirements
Must have
- Final design language must be in German, basically, the Title Description needs to be "Physiotherapeutin" the other details remain as in the English Language.
Nice to have
- Simple, modern, minimalist design
Should not have
- too many colors, Obvious use of a skeleton, skull, spline

```html
<!DOCTYPE html>
<html lang="de">
<head>
<meta charset="utf-8">
<title>Lilla Varga – Physiotherapeutin</title>
<link rel="stylesheet" href="https://fonts.googleapis.com/css2?family=Saira+Condensed:wght@300;700&family=Open+Sans:wght@400&display=swap">
<style>
  :root {
    --page-bg: #e9e6e2;
    --card-bg: #050505;
    --ink: #ffffff;
  }
  * { margin: 0; padding: 0; box-sizing: border-box; }
  html, body {
    width: 1200px;
    height: 1200px;
    overflow: hidden;
    background: var(--page-bg);
  }
  .canvas {
    position: relative;
    width: 1200px;
    height: 1200px;
  }
  .business-card {
    position: absolute;
    left: 250px;
    top: 60px;
    width: 700px;
    height: 1080px;
    background: var(--card-bg);
    color: var(--ink);
    overflow: hidden;
  }
  .card-art {
    position: absolute;
    inset: 0;
    width: 700px;
    height: 1080px;
  }
  .card-frame path {
    fill: none;
    stroke: var(--ink);
    stroke-width: 4;
  }
  .headline text {
    fill: var(--ink);
    font-family: "Saira Condensed", "Arial Narrow", sans-serif;
    font-size: 100px;
  }
  .headline .job-title { font-weight: 700; }
  .headline .person-name { font-weight: 300; }
  .contact-block {
    position: absolute;
    left: 80px;
    bottom: 92px;
    font-family: "Open Sans", Arial, sans-serif;
    font-style: normal;
    font-size: 24px;
    letter-spacing: 0.2em;
    line-height: 1.3;
  }
  .contact-block p { white-space: nowrap; }
</style>
</head>
<body>
  <main class="canvas">
    <article class="business-card">
      <svg class="card-art" viewBox="0 0 700 1080" role="group" aria-label="Physiotherapeutin Lilla Varga">
        <g class="card-frame" aria-hidden="true">
          <path d="M22 420 V22 H678 V160"/>
          <path d="M678 230 V560"/>
          <path d="M678 640 V1058 H22 V930"/>
          <path d="M22 500 V860"/>
        </g>
        <g class="headline">
          <text class="job-title" x="80" y="200" textLength="440" lengthAdjust="spacingAndGlyphs">PHYSIOTHE</text>
          <text class="job-title" x="80" y="285" textLength="440" lengthAdjust="spacingAndGlyphs">RAPEUTIN</text>
          <text class="person-name" x="80" y="370" textLength="230" lengthAdjust="spacingAndGlyphs">LILLA</text>
          <text class="person-name" x="80" y="455" textLength="275" lengthAdjust="spacingAndGlyphs">VARGA</text>
        </g>
      </svg>

      <address class="contact-block">
        <p class="contact-role">Physiotherapist</p>
        <p class="contact-phone">+43 664 5290 4816</p>
        <p class="contact-email">lilla.praxis@brelomail.com</p>
      </address>
    </article>
  </main>
</body>
</html>
```